Book cover for a book about time management for women

We need a book cover for a book about time management for women written by a woman. Even though the book has a provocative title "Calendar candy" based on the seminars the author holds for women seeking the change in their life, it has nothing to do with the words themselves. The subtitle is "Keep each morning in your grip. A bold guide on daily rhythm for ladies today"

Preferred fonts (not necessarily):
Plus Jakarta Sans
Tiempos Headline

Preferred colours (not necessarily):
- orange
- pastel "highlighters"

We look for a simple/clean design that catches the attention of the women without too many graphic elements.

Target Market(s)

Women that want to change and organise their life

Industry/Entity Type

productivity, marketing, work-life balance

Font styles to use
Other font styles liked:
• Plus Jakarta Sans, Tiempos Headline

Colors
F0912C
F2A743
F7CA91
FBE8D2
FDF5EE
A7469A
B969AE
D3A5CF
EDDBEB
F8F0F9

Requirements
Must have
• Famine feeling as the target audience are women with drive to better life
Should not have
• No explicit images or sexually motivated themes

```html
<!DOCTYPE html>
<html lang="en">
<head>
<meta charset="utf-8">
<title>Calendar Candy – Book Cover</title>
<link rel="stylesheet" href="https://fonts.googleapis.com/css2?family=Source+Serif+4:opsz,wght@8..60,900&family=Plus+Jakarta+Sans:wght@500;600&display=swap">
<style>
  :root {
    --backdrop: #e5e5e5;
    --cover-lilac: #c399c0;
    --title-plum: #99408f;
    --ink: #111111;
    --sunset-orange: #d97a2e;
    --dusk-ground: #101a0c;
    --author-white: #f6f2ee;
  }
  * { margin: 0; padding: 0; box-sizing: border-box; }
  html, body {
    width: 1200px;
    height: 800px;
    overflow: hidden;
    background: var(--backdrop);
  }
  .canvas {
    position: relative;
    width: 1200px;
    height: 800px;
  }
  .book-cover {
    position: absolute;
    left: 365px;
    top: 40px;
    width: 470px;
    height: 720px;
    background: var(--cover-lilac);
    overflow: hidden;
  }
  .cover-title {
    position: absolute;
    top: 136px;
    left: 0;
    width: 100%;
    text-align: center;
    font-family: "Source Serif 4", Georgia, serif;
    font-weight: 900;
    color: var(--title-plum);
    text-transform: uppercase;
    line-height: 0.95;
  }
  .cover-title .title-line-top {
    display: block;
    font-size: 76px;
    letter-spacing: -1px;
  }
  .cover-title .title-line-main {
    display: block;
    font-size: 118px;
    letter-spacing: -3px;
  }
  .cover-subtitle {
    position: absolute;
    top: 398px;
    left: 0;
    width: 100%;
    text-align: center;
    font-family: "Plus Jakarta Sans", Arial, sans-serif;
    color: var(--ink);
    text-transform: uppercase;
  }
  .cover-subtitle .subtitle-lead {
    display: block;
    font-weight: 600;
    font-size: 16px;
    letter-spacing: 1.6px;
  }
  .cover-subtitle .subtitle-tagline {
    display: block;
    margin-top: 8px;
    font-weight: 500;
    font-size: 11px;
    letter-spacing: 1.2px;
  }
  .cover-photo {
    position: absolute;
    left: 0;
    top: 470px;
    width: 100%;
    height: 250px;
    background: linear-gradient(to bottom,
      var(--cover-lilac) 0%,
      var(--sunset-orange) 40%,
      var(--dusk-ground) 65%,
      var(--dusk-ground) 100%);
  }
  .cover-author {
    position: absolute;
    top: 654px;
    left: 0;
    width: 100%;
    text-align: center;
    font-family: "Plus Jakarta Sans", Arial, sans-serif;
    font-weight: 500;
    font-size: 28px;
    letter-spacing: 2.5px;
    color: var(--author-white);
    text-transform: uppercase;
  }
</style>
</head>
<body>
  <main class="canvas">
    <article class="book-cover">
      <div class="cover-photo" role="img" aria-label="Photo placeholder: silhouette of a woman with flowing hair before an orange sunset over dark hills"></div>
      <h1 class="cover-title">
        <span class="title-line-top">Calendar</span>
        <span class="title-line-main">Candy</span>
      </h1>
      <p class="cover-subtitle">
        <span class="subtitle-lead">Keep each morning in your grip.</span>
        <span class="subtitle-tagline">A bold guide on daily rhythm for ladies today</span>
      </p>
      <p class="cover-author">Author Name</p>
    </article>
  </main>
</body>
</html>
```